Property investment company needs a letterhead design!

We are a new residential and commercial property investment company. Name of the company is Morvesta Group, LLC. We have a new logo and now we need letterhead! We prefer to have a professional and upscale appearance. We don't have any fixed requirements, so be creative! Thank you for considering this project. We are so excited to see what happens!

Target Market(s)

Professional

Industry/Entity Type

Real Estate Development

```html
<!DOCTYPE html>
<html lang="en">
<head>
<meta charset="utf-8">
<title>Morvesta Group, LLC — Letterhead</title>
<link rel="stylesheet" href="https://fonts.googleapis.com/css2?family=Montserrat:wght@700&display=swap">
<style>
  :root {
    --navy: #001641;
    --sky: #00ccff;
    --aqua: #00ffff;
    --mist: #f6f6f6;
    --paper: #ffffff;
    --ghost: #eff0f5;
  }
  html, body {
    margin: 0;
    padding: 0;
    overflow: hidden;
    background: var(--paper);
  }
  .letterhead {
    position: relative;
    width: 856px;
    height: 1200px;
    overflow: hidden;
    background: var(--paper);
    font-family: "Montserrat", Arial, sans-serif;
  }
  .corner-art {
    position: absolute;
    inset: 0;
    width: 856px;
    height: 1200px;
  }
  .fill-mist { fill: var(--mist); }
  .fill-navy { fill: var(--navy); }
  .fill-sky { fill: var(--sky); }
  .fill-aqua { fill: var(--aqua); }

  .brand {
    position: absolute;
    top: 62px;
    right: 64px;
    width: 120px;
    display: flex;
    flex-direction: column;
    align-items: center;
    gap: 6px;
    color: var(--navy);
    font-weight: 700;
    text-align: center;
  }
  .brand-dot {
    width: 38px;
    height: 38px;
    border-radius: 50%;
    background: var(--navy);
  }
  .brand-name {
    font-size: 15px;
    letter-spacing: 0.5px;
    line-height: 1.1;
  }
  .brand-sub {
    font-size: 8px;
    letter-spacing: 2px;
  }

  .backdrop-name {
    position: absolute;
    top: 540px;
    left: 0;
    width: 856px;
    text-align: center;
    color: var(--ghost);
    font-weight: 700;
  }
  .backdrop-name .word {
    display: block;
    font-size: 50px;
    letter-spacing: 1px;
    line-height: 1;
  }
  .backdrop-name .sub {
    display: block;
    margin-top: 18px;
    font-size: 22px;
    letter-spacing: 8px;
  }
</style>
</head>
<body>
  <main class="letterhead">
    <svg class="corner-art" viewBox="0 0 856 1200" aria-hidden="true">
      <g class="corner-top-left">
        <polygon class="fill-mist" points="0,0 319,0 370,29.5 0,242"/>
        <polygon class="fill-navy" points="0,0 152,0 230,45 0,178"/>
        <polygon class="fill-aqua" points="0,21 29,38 29,146 0,162"/>
        <polygon class="fill-sky" points="29,18 170,100 29,181"/>
      </g>
      <g class="corner-bottom-right">
        <polygon class="fill-mist" points="856,958 485,1170 538,1200 856,1200"/>
        <polygon class="fill-navy" points="856,1021 626,1154 704,1200 856,1200"/>
        <polygon class="fill-aqua" points="826,1054 856,1037 856,1178 826,1162"/>
        <polygon class="fill-sky" points="826,1019 685,1099 826,1181"/>
      </g>
    </svg>

    <div class="brand">
      <span class="brand-dot"></span>
      <span class="brand-name">MORVESTA</span>
      <span class="brand-sub">GROUP, LLC</span>
    </div>

    <div class="backdrop-name" aria-hidden="true">
      <span class="word">MORVESTA</span>
      <span class="sub">GROUP, LLC</span>
    </div>
  </main>
</body>
</html>
```